I need to redesign this website. Modern Fun Professional Redesign For www.JollyPerkHub.com = New Name www.ClaimVouchly.com

Use existing content as it is on website exactly and we will revise after initial mock ups.

The new name will be ClaimVouchly.com please make a quick logo for this site too while redesigning.

Make it look like an official website....

Target Market(s)

Consumers that are redeeming certificates that businesses gave to them as a gift for customer loyalty,e tc.

Industry/Entity Type

It Professional

Logo Text

www.ClaimVouchly.com

Number of Pages Required

4 page

Colors

Designer to choose colors to be used in the design.

Requirements
Must have
• Must look professional, build trust and credibility.
Nice to have
• open
Should not have
• open

```html
<!DOCTYPE html>
<html lang="en">
<head>
<meta charset="utf-8">
<title>Claim Vouchly</title>
<link href="https://fonts.googleapis.com/css2?family=Lora:wght@400;700&family=Open+Sans:wght@400;600&display=swap" rel="stylesheet">
<style>
:root{
  --teal:#40b8c7;
  --gold:#c89a30;
  --green:#3b6e12;
  --ink:#2b2b2b;
  --text:#555;
  --footer:#262626;
  --white:#fff;
}
*{margin:0;padding:0;box-sizing:border-box}
html,body{width:1200px;height:2671px;overflow:hidden;background:var(--white)}
body{position:relative;font-family:'Open Sans',Arial,sans-serif;color:var(--text)}
.abs{position:absolute}
.serif{font-family:'Lora',Georgia,serif}

/* header */
.site-header{left:0;top:0;width:1200px;height:118px;background:var(--white)}
.brand{left:100px;top:34px;display:flex;align-items:center;gap:14px}
.brand-mark{width:36px;height:36px;background:var(--gold);border-radius:4px}
.brand-name{font-family:'Lora',Georgia,serif;font-weight:700;font-size:34px;color:var(--teal)}
.nav{left:712px;top:44px;display:flex;align-items:center;gap:40px;font-family:'Lora',Georgia,serif;font-size:14px;font-weight:700;color:var(--ink)}
.nav .active{background:var(--teal);color:var(--white);padding:7px 26px;border-radius:18px}

/* hero */
.hero{left:0;top:118px;width:1200px;height:600px;background:linear-gradient(180deg,#3d6f99 0%,#5fa4c4 30%,#3bbfc4 48%,#6d5a45 68%,#8a7560 100%)}
.hero-panel{left:98px;top:315px;width:545px;height:170px;background:rgba(40,40,40,.45)}
.hero-title{left:123px;top:337px;font-family:'Lora',Georgia,serif;font-weight:700;font-size:17px;color:var(--white);letter-spacing:.5px;text-transform:uppercase}
.hero-sub{left:123px;top:376px;font-family:'Lora',Georgia,serif;font-size:12.5px;color:var(--white)}
.search{left:121px;top:425px;width:498px;height:48px;background:var(--white);border-radius:24px;border:3px solid var(--white)}
.search-placeholder{left:26px;top:11px;font-size:13px;color:#777}
.search-btn{right:0;top:0;width:138px;height:42px;background:var(--gold);border-radius:21px;color:var(--white);font-family:'Lora',Georgia,serif;font-weight:700;font-size:16px;display:flex;align-items:center;justify-content:center}
.hero-wave{left:0;top:590px}

/* welcome */
.welcome-title{left:0;top:752px;width:1200px;text-align:center;font-family:'Lora',Georgia,serif;font-weight:700;font-size:32px;color:var(--ink)}
.swoosh{left:452px}
.welcome-text{left:0;top:852px;width:1200px;text-align:center;font-size:13px;line-height:27px;color:var(--text)}
.feature{top:950px;width:300px;text-align:center}
.feature-circle{margin:0 auto;width:200px;height:200px;border-radius:50%;background:var(--teal);display:flex;align-items:center;justify-content:center}
.feature-ring{width:178px;height:178px;border-radius:50%;border:2px solid var(--white);display:flex;align-items:center;justify-content:center}
.feature-title{margin-top:30px;font-family:'Lora',Georgia,serif;font-weight:700;font-size:20px;color:var(--ink)}
.feature-text{margin-top:10px;font-size:13px;line-height:27px;color:var(--text)}

/* request */
.request{left:0;top:1318px}
.request-title{left:0;top:1412px;width:1200px;text-align:center;font-family:'Lora',Georgia,serif;font-weight:700;font-size:29px;color:var(--white)}
.field{width:358px;height:34px;background:var(--white);border-radius:17px;padding:9px 20px;font-size:12px;color:#666}
.send{left:525px;top:1618px;width:144px;height:40px;border:1px solid var(--white);border-radius:20px;color:var(--white);font-family:'Lora',Georgia,serif;font-size:14px;display:flex;align-items:center;justify-content:center}

/* testimonials */
.test-title{left:0;top:1757px;width:1200px;text-align:center;font-family:'Lora',Georgia,serif;font-weight:700;font-size:30px;color:var(--ink)}
.card{top:1876px;width:321px;height:377px;border:1px solid #e2e2e2;background:var(--white)}
.card-head{height:142px;background:var(--teal);position:relative}
.avatar{position:absolute;left:23px;top:14px;width:106px;height:106px;border-radius:50%;background:linear-gradient(160deg,#d8cfc4,#6b7a8a)}
.card-name{position:absolute;left:150px;top:37px;font-family:'Lora',Georgia,serif;font-weight:700;font-size:15px;color:var(--white)}
.card-role{position:absolute;left:150px;top:72px;font-size:12.5px;color:var(--white)}
.quote{margin:34px 0 0 18px;width:34px;height:26px}
.card-text{margin:10px 18px 0 18px;font-size:12.5px;line-height:27px;color:var(--text)}

/* footer */
.footer{left:0;top:2305px}
.footer-brand{left:0;top:2372px;width:1200px;display:flex;justify-content:center;align-items:center;gap:14px}
.footer-brand .brand-name{color:var(--white)}
.icon-dot{width:40px;height:40px;border-radius:50%;background:var(--white);display:flex;align-items:center;justify-content:center}
.address{left:153px;top:2494px;font-size:12.5px;line-height:27px;color:var(--white);font-weight:600}
.social{width:38px;height:38px;border-radius:50%}
.phone{left:981px;top:2496px;font-size:20px;font-weight:600;color:var(--white)}
.divider{left:98px;top:2613px;width:1004px;height:1px;background:#444}
.copyright{left:0;top:2632px;width:1200px;text-align:center;font-family:'Lora',Georgia,serif;font-size:12px;color:var(--white)}
</style>
</head>
<body>

<header class="site-header abs">
  <div class="brand abs"><span class="brand-mark"></span><span class="brand-name">Claim Vouchly</span></div>
  <nav class="nav abs">
    <span class="active">Home</span><span>Contact Us</span><span>Testimonials</span><span>Terms</span>
  </nav>
</header>

<section class="hero abs" role="img" aria-label="Couple in white sitting on a wooden pier beside an overwater bungalow, facing a turquoise sea"></section>
<div class="hero-panel abs"></div>
<div class="hero-title abs">Enter a valid certificate ID in the form below</div>
<div class="hero-sub abs">To Redeem Your Certificate And To View Faq'S, Terms And Locations.</div>
<div class="search abs">
  <span class="search-placeholder abs">Certificate ID...</span>
  <span class="search-btn abs">Search</span>
</div>
<svg class="hero-wave abs" width="1200" height="140" viewBox="0 0 1200 140">
  <path d="M0 20 C300 45 500 10 760 38 C950 58 1080 30 1200 12 L1200 140 L0 140 Z" fill="#fff"/>
  <path d="M0 22 C300 45 500 12 760 38 C950 58 1080 30 1200 12" fill="none" stroke="var(--green)" stroke-width="8"/>
  <path d="M0 118 C250 135 450 110 620 70 C800 30 1000 20 1200 40" fill="none" stroke="var(--teal)" stroke-width="9"/>
  <path d="M0 108 C250 125 450 100 620 62 C800 24 1000 14 1200 32 L1200 22 C1000 6 800 18 620 54 C450 92 250 118 0 98 Z" fill="#fff"/>
</svg>

<h1 class="welcome-title abs">Welcome To The Claim Vouchly</h1>
<svg class="swoosh abs" style="top:806px" width="296" height="14" viewBox="0 0 296 14"><path d="M0 10 C90 0 210 0 296 8 C210 4 90 6 0 10Z" fill="var(--ink)"/></svg>
<p class="welcome-text abs">Lorem ipsum dolor sit amet, consectetur adipiscing elit, sed do eiusmod tempor incididunt ut labore et dolore magna aliqua.<br>Ut enim ad minim veniam, quis nostrud exercitation ullamco laboris nisi ut aliquip ex ea commodo consequat.</p>

<div class="feature abs" style="left:64px">
  <div class="feature-circle"><div class="feature-ring">
    <svg width="80" height="74" viewBox="0 0 80 74" fill="none" stroke="#fff" stroke-width="4"><rect x="4" y="10" width="72" height="60" rx="3"/><line x1="4" y1="24" x2="76" y2="24"/><line x1="20" y1="3" x2="20" y2="16"/><line x1="40" y1="3" x2="40" y2="16"/><line x1="60" y1="3" x2="60" y2="16"/><rect x="32" y="36" width="16" height="14"/><line x1="14" y1="38" x2="22" y2="38"/><line x1="14" y1="50" x2="22" y2="50"/><line x1="56" y1="38" x2="66" y2="38"/><line x1="56" y1="50" x2="66" y2="50"/><line x1="14" y1="60" x2="66" y2="60"/></svg>
  </div></div>
  <div class="feature-title">Flexible Schedule</div>
  <div class="feature-text">Lorem Ipsum is that it has a more-or-less<br>normal distribution of letters,</div>
</div>
<div class="feature abs" style="left:452px">
  <div class="feature-circle"><div class="feature-ring">
    <svg width="100" height="80" viewBox="0 0 100 80" fill="none" stroke="#fff" stroke-width="5"><path d="M38 14 A30 30 0 1 0 38 66"/><path d="M32 6 L42 14 L32 22" stroke-linejoin="round"/><text x="42" y="54" font-family="Open Sans,Arial,sans-serif" font-size="34" font-weight="600" fill="#fff" stroke="none">24</text></svg>
  </div></div>
  <div class="feature-title">Customer Support</div>
  <div class="feature-text">Lorem Ipsum is that it has a more-or-less<br>normal distribution of letters,</div>
</div>
<div class="feature abs" style="left:838px">
  <div class="feature-circle"><div class="feature-ring">
    <svg width="110" height="50" viewBox="0 0 110 50"><polygon points="18,6 23,18 36,18 26,26 30,39 18,31 6,39 10,26 0,18 13,18" fill="#fff"/><polygon points="55,10 61,24 76,24 64,33 69,48 55,39 41,48 46,33 34,24 49,24" fill="none" stroke="#fff" stroke-width="3"/><polygon points="92,6 97,18 110,18 100,26 104,39 92,31 80,39 84,26 74,18 87,18" fill="#fff"/></svg>
  </div></div>
  <div class="feature-title">Best Reviews</div>
  <div class="feature-text">Lorem Ipsum is that it has a more-or-less<br>normal distribution of letters,</div>
</div>

<svg class="request abs" width="1200" height="392" viewBox="0 0 1200 392"><path d="M0 30 C200 0 420 18 620 8 C820 0 1000 30 1200 14 L1200 392 L0 392 Z" fill="var(--gold)"/></svg>
<h2 class="request-title abs">Request to redeem your certificate</h2>
<div class="field abs" style="left:224px;top:1499px">Name...</div>
<div class="field abs" style="left:618px;top:1499px">Email....</div>
<div class="field abs" style="left:224px;top:1559px">Contact Number</div>
<div class="field abs" style="left:618px;top:1559px">Purpose</div>
<div class="send abs">SEND REQUEST</div>

<h2 class="test-title abs">Our Testimonials</h2>
<svg class="swoosh abs" style="left:492px;top:1813px" width="216" height="14" viewBox="0 0 216 14"><path d="M0 10 C70 0 150 0 216 6 C150 4 70 6 0 10Z" fill="var(--ink)"/></svg>

<div class="card abs" style="left:98px">
  <div class="card-head"><div class="avatar" role="img" aria-label="Portrait of a customer"></div><div class="card-name">Perferendis Doloribus</div><div class="card-role">Lorem Ipsum is dummy</div></div>
  <svg class="quote" viewBox="0 0 34 26"><path d="M0 26V12C0 5 4 1 12 0v5C8 6 7 8 7 12h7v14ZM20 26V12c0-7 4-11 12-12v5c-4 1-5 3-5 7h7v14Z" fill="#999"/></svg>
  <p class="card-text">Lorem Ipsum has been the industry's &nbsp;can standard dummy text ever since the 1500s, when an unknown printer took a galley of type and scrambled it to make a type &nbsp;of the specimen book. It has survived typesetting,</p>
</div>
<div class="card abs" style="left:440px">
  <div class="card-head"><div class="avatar" role="img" aria-label="Portrait of a customer"></div><div class="card-name">Perferendis Doloribus</div><div class="card-role">Lorem Ipsum is dummy</div></div>
  <svg class="quote" viewBox="0 0 34 26"><path d="M0 26V12C0 5 4 1 12 0v5C8 6 7 8 7 12h7v14ZM20 26V12c0-7 4-11 12-12v5c-4 1-5 3-5 7h7v14Z" fill="#999"/></svg>
  <p class="card-text">Lorem Ipsum has been the industry's &nbsp;can standard dummy text ever since the 1500s, when an unknown printer took a galley of type and scrambled it to make a type &nbsp;of the specimen book. It has survived typesetting,</p>
</div>
<div class="card abs" style="left:780px">
  <div class="card-head"><div class="avatar" role="img" aria-label="Portrait of a customer"></div><div class="card-name">Perferendis Doloribus</div><div class="card-role">Lorem Ipsum is dummy</div></div>
  <svg class="quote" viewBox="0 0 34 26"><path d="M0 26V12C0 5 4 1 12 0v5C8 6 7 8 7 12h7v14ZM20 26V12c0-7 4-11 12-12v5c-4 1-5 3-5 7h7v14Z" fill="#999"/></svg>
  <p class="card-text">Lorem Ipsum has been the industry's &nbsp;can standard dummy text ever since the 1500s, when an unknown printer took a galley of type and scrambled it to make a type &nbsp;of the specimen book. It has survived typesetting,</p>
</div>

<svg class="footer abs" width="1200" height="366" viewBox="0 0 1200 366"><path d="M0 22 C300 0 700 -4 1200 20 L1200 366 L0 366 Z" fill="var(--footer)"/></svg>
<div class="footer-brand abs"><span class="brand-mark"></span><span class="brand-name">Claim Vouchly</span></div>

<div class="icon-dot abs" style="left:98px;top:2490px">
  <svg width="14" height="18" viewBox="0 0 14 18"><path d="M7 0A7 7 0 0 0 0 7c0 5 7 11 7 11s7-6 7-11A7 7 0 0 0 7 0Zm0 10a3 3 0 1 1 0-6 3 3 0 0 1 0 6Z" fill="var(--gold)"/></svg>
</div>
<div class="address abs">The Voucher Desk<br>4521 Harbor View Ave Ste B #210<br>Bayfield, Ca 90000</div>

<span class="social abs" style="left:529px;top:2491px;background:#2d5aa0"></span>
<span class="social abs" style="left:581px;top:2491px;background:#1da6e0"></span>
<span class="social abs" style="left:633px;top:2491px;background:#a0780f"></span>

<div class="icon-dot abs" style="left:925px;top:2490px">
  <svg width="16" height="12" viewBox="0 0 16 12"><rect width="16" height="12" rx="1" fill="var(--gold)"/><path d="M0 1l8 6 8-6" fill="none" stroke="#fff" stroke-width="1.4"/></svg>
</div>
<div class="phone abs">555 014 2736</div>

<div class="divider abs"></div>
<div class="copyright abs">Copyright © 2017 ClaimVouchly.Allrights reserved.</div>

</body>
</html>
```